Create website design - Hire business

Build website to specification. Look and feel only or include all functionality. I have put together a google document which includes all information on requirements. I will share this with you via message once you have been assigned the job.

Coding

Coded - Design and coding required

Number of Pages Required

1 page

Requirements
Must have
• As per Google Doc
Nice to have
• As per Google Doc
Should not have
• As per Google Doc

```html
<!DOCTYPE html>
<html lang="en">
<head>
<meta charset="utf-8">
<title>Kerbside Hire</title>
<link href="https://fonts.googleapis.com/css2?family=Fraunces:opsz,wght@9..144,700;9..144,800&family=Roboto:wght@400;500;700&display=swap" rel="stylesheet">
<style>
:root{
  --teal:#1f6f6b;
  --teal-dark:#175c58;
  --blue:#0e67b0;
  --blue-dark:#0b5697;
  --ink:#111111;
  --muted:#6d6d6d;
  --line:#e6e6e6;
  --star:#e8901c;
  --footer:#0b0b0b;
  --white:#ffffff;
}
*{box-sizing:border-box;margin:0;padding:0}
html,body{width:1200px;height:5055px;overflow:hidden;background:var(--white)}
body{position:relative;font-family:"Roboto",Arial,sans-serif;color:var(--ink)}
.abs{position:absolute}
.serif{font-family:"Fraunces",Georgia,serif;font-weight:800}
.center{text-align:center}
.btn{position:absolute;display:flex;align-items:center;justify-content:center;border-radius:24px;color:#fff;font-weight:500}

/* header */
.topline{left:0;top:0;width:1200px;height:4px;background:var(--teal)}
.brand{left:110px;top:36px;font-size:27px;color:var(--teal)}
.nav{top:44px;font-size:13px;color:#222;font-weight:500}
.btn-touch{left:959px;top:33px;width:130px;height:40px;background:var(--teal);font-size:13px}

/* hero */
.hero{left:112px;top:112px;width:977px;height:535px;border-radius:0 0 88px 88px;
  background:linear-gradient(160deg,#22321f 0%,#3f5a2c 35%,#6b5234 55%,#2f5526 75%,#1d3a1b 100%)}
.hero-title{left:177px;top:232px;font-size:55px;line-height:68px;color:#fff}
.btn-start{left:177px;top:396px;width:125px;height:42px;background:var(--blue);font-size:13px}
.search{left:173px;top:600px;width:855px;height:100px;background:#fff;border-radius:0 0 40px 40px;box-shadow:0 8px 22px rgba(0,0,0,.12)}
.field-label{top:618px;font-size:12px;font-weight:500;color:#222}
.field{top:647px;width:167px;height:34px;background:#f1f1f1;border-radius:4px;font-size:11px;color:#777;display:flex;align-items:center;padding-left:40px}
.field svg{position:absolute;left:14px;top:10px}
.field .caret{position:absolute;right:12px;top:14px}
.search-go{left:959px;top:643px;width:40px;height:40px;border-radius:50%;background:var(--teal);display:flex;align-items:center;justify-content:center}

/* about */
.about-h{left:141px;top:790px;font-size:40px}
.about-lead{left:141px;top:856px;width:420px;font-size:24px;line-height:37px;font-family:"Fraunces",Georgia,serif;font-weight:700}
.about-lead span{color:var(--blue)}
.about-copy{left:614px;top:792px;width:455px;font-size:13.5px;line-height:28.5px;color:var(--muted)}
.about-copy p+p{margin-top:28px}
.btn-read{left:616px;top:1069px;width:128px;height:41px;background:var(--blue);font-size:14px}
.frame{background:#fff;padding:8px;border-radius:14px;box-shadow:0 6px 22px rgba(0,0,0,.16)}
.frame div{width:100%;height:100%;border-radius:8px}

/* section headings */
.sec-h{left:0;width:1200px;font-size:40px}
.sec-p{left:180px;width:840px;font-size:14px;line-height:28px;color:var(--muted)}

/* categories */
.cat{width:231px;height:397px;background:#fff;border:1px solid var(--line);border-radius:6px;box-shadow:0 4px 14px rgba(0,0,0,.06)}
.cat-img{position:absolute;left:12px;top:12px;width:207px;height:192px;border-radius:0 0 90px 90px/0 0 30px 30px}
.cat-icon{position:absolute;left:86px;top:158px;width:60px;height:60px;border-radius:50%;background:#fff;display:flex;align-items:center;justify-content:center}
.cat-t{position:absolute;left:0;top:240px;width:100%;text-align:center;font-size:17px;font-weight:500}
.cat-d{position:absolute;left:18px;top:275px;width:195px;text-align:center;font-size:12px;line-height:22px;color:var(--muted)}
.cat-l{position:absolute;left:0;top:354px;width:100%;text-align:center;font-size:13px;font-weight:700;color:var(--blue);text-decoration:underline}
.dot{width:28px;height:28px;border-radius:50%;display:flex;align-items:center;justify-content:center}
.dot.off{background:#7a7a7a}.dot.on{background:#000}

/* why */
.why{left:112px;top:2341px;width:977px;height:445px;border-radius:80px;background:linear-gradient(135deg,#1a6fb8,#0c5fa6 55%,#0a4f8d)}
.why-h{top:2400px;color:#fff}
.why-p{top:2464px;color:#e4eef8;left:200px;width:800px}
.why-ring{width:102px;height:102px;border-radius:50%;border:2px dashed #fff;display:flex;align-items:center;justify-content:center}
.why-ring div{width:74px;height:74px;border-radius:50%;background:#fff;display:flex;align-items:center;justify-content:center}
.why-l{top:2700px;width:260px;text-align:center;color:#fff;font-size:14.5px}

/* testimonials */
.quote{width:310px;height:336px;background:#fff;border-radius:8px;box-shadow:0 4px 20px rgba(0,0,0,.09)}
.avatar{position:absolute;left:32px;top:36px;width:66px;height:66px;border-radius:50%}
.q-name{position:absolute;left:32px;top:124px;font-size:17px}
.q-text{position:absolute;left:32px;top:155px;width:250px;font-size:11.5px;line-height:22.5px;color:var(--muted)}
.stars{position:absolute;left:32px;top:276px;font-size:14px;color:var(--star);letter-spacing:1px}
.q-badge{position:absolute;top:272px;width:26px;height:26px;border-radius:50%}

/* newsletter */
.news{left:112px;top:3551px;width:977px;height:359px;border-radius:80px;background:linear-gradient(135deg,#227771,#1c6460)}
.news-h{top:3600px;color:#fff}
.news-p{top:3667px;left:200px;width:800px;color:#e3f0ef}
.news-s{left:0;top:3738px;width:1200px;font-size:19px;font-family:"Fraunces",Georgia,serif;font-weight:700;color:#fff}
.news-in{left:330px;top:3806px;width:539px;height:43px;background:#fff;border-radius:24px;font-size:12px;color:#777;padding-left:30px;display:flex;align-items:center}
.news-btn{left:700px;top:3806px;width:169px;height:43px;background:var(--blue);font-size:13px}

/* blogs */
.b-img{width:314px;height:217px}
.b-card{width:277px;height:263px;background:#fff;border-radius:12px;box-shadow:0 6px 20px rgba(0,0,0,.08)}
.b-date{position:absolute;left:21px;top:36px;width:104px;height:29px;border-radius:15px;background:var(--teal);color:#fff;font-size:11px;font-weight:500;display:flex;align-items:center;justify-content:center}
.b-t{position:absolute;left:21px;top:84px;width:245px;font-size:13.5px;line-height:24px;font-weight:500}
.b-d{position:absolute;left:21px;top:141px;width:240px;font-size:11.5px;line-height:22px;color:var(--muted)}
.b-l{position:absolute;left:21px;top:222px;font-size:12px;font-weight:700;color:var(--blue);text-decoration:underline}

/* footer */
.footer{left:0;top:4679px;width:1200px;height:376px;background:var(--footer);border-radius:100px 100px 0 0}
.f-brand{left:149px;top:4812px;font-size:26px;color:#fff}
.social{top:4872px;width:38px;height:38px;border-radius:50%;background:var(--blue)}
.f-h{top:4760px;font-size:18px;color:#fff;font-family:"Fraunces",Georgia,serif;font-weight:700}
.f-t{font-size:13px;color:#e8e8e8;line-height:27px}
.f-link{font-size:13px;color:#e8e8e8}
.copy{left:0;top:5012px;width:1200px;font-size:11px;color:#ddd}
</style>
</head>
<body>

<header>
  <div class="abs topline"></div>
  <div class="abs brand serif">Kerbside Hire</div>
  <nav>
    <span class="abs nav" style="left:390px">About</span>
    <span class="abs nav" style="left:482px">Our Services</span>
    <span class="abs nav" style="left:614px">Privacy Policy</span>
    <span class="abs nav" style="left:755px">Terms</span>
    <span class="abs nav" style="left:848px">Contact Us</span>
  </nav>
  <div class="btn btn-touch">Get In Touch</div>
</header>

<section class="hero-block">
  <div class="abs hero" role="img" aria-label="Wooden gazebo in a lush forest garden"></div>
  <h1 class="abs hero-title serif">Welcome To<br>Kerbside Hire</h1>
  <div class="btn btn-start">Get Started</div>

  <div class="abs search"></div>
  <span class="abs field-label" style="left:206px">Location</span>
  <span class="abs field-label" style="left:392px">Select Service</span>
  <span class="abs field-label" style="left:581px">From (Date)</span>
  <span class="abs field-label" style="left:769px">To (Date)</span>

  <div class="abs field" style="left:206px">
    <svg width="12" height="14" viewBox="0 0 12 14"><path d="M6 0C2.7 0 0 2.6 0 5.8 0 10 6 14 6 14s6-4 6-8.2C12 2.6 9.3 0 6 0zm0 8a2.2 2.2 0 110-4.4A2.2 2.2 0 016 8z" fill="var(--teal)"/></svg>Select
    <svg class="caret" width="8" height="5"><path d="M0 0h8L4 5z" fill="#666"/></svg>
  </div>
  <div class="abs field" style="left:392px;width:171px">
    <svg width="14" height="14" viewBox="0 0 14 14"><circle cx="7" cy="7" r="5" fill="none" stroke="var(--teal)" stroke-width="3" stroke-dasharray="3 2"/><circle cx="7" cy="7" r="2" fill="var(--teal)"/></svg>Choose Here
    <svg class="caret" width="8" height="5"><path d="M0 0h8L4 5z" fill="#666"/></svg>
  </div>
  <div class="abs field" style="left:581px;width:170px">
    <svg width="13" height="13" viewBox="0 0 13 13"><rect x="0" y="2" width="13" height="11" rx="2" fill="var(--teal)"/><rect x="2" y="6" width="9" height="5" fill="#fff"/></svg>Select
    <svg class="caret" width="8" height="5"><path d="M0 0h8L4 5z" fill="#666"/></svg>
  </div>
  <div class="abs field" style="left:769px;width:171px">
    <svg width="13" height="13" viewBox="0 0 13 13"><rect x="0" y="2" width="13" height="11" rx="2" fill="var(--teal)"/><rect x="2" y="6" width="9" height="5" fill="#fff"/></svg>Select
    <svg class="caret" width="8" height="5"><path d="M0 0h8L4 5z" fill="#666"/></svg>
  </div>
  <div class="abs search-go"><svg width="16" height="16" viewBox="0 0 16 16"><circle cx="7" cy="7" r="5" fill="none" stroke="#fff" stroke-width="2"/><path d="M11 11l4 4" stroke="#fff" stroke-width="2"/></svg></div>
</section>

<section class="about">
  <h2 class="abs about-h serif">About Us</h2>
  <p class="abs about-lead">Sed ut perspiciatis unde omnis iste natus error <span>sit voluptatem</span> accusa ntium doloremque laudantium, <span>totam rem aperiam</span></p>
  <div class="abs about-copy">
    <p>I must explain to you how all this mistaken idea of denouncing pleasure and praising pain was born and I will give you a complete account of the system, and expound the actual teachings of the great explorer of the truth, the master-builder of human happiness. No one rejects, dislikes, or avoids pleasure itself</p>
    <p>Because it is pleasure, but because those who do not know how to pursue pleasure rationally encounter consequences that are extremely painful. Nor again is there anyone</p>
  </div>
  <div class="btn btn-read">Read More</div>
  <div class="abs frame" style="left:141px;top:1046px;width:428px;height:341px"><div role="img" aria-label="Man relaxing in a garden chair beside a modern house" style="background:linear-gradient(180deg,#b9cde4 0%,#cfd6d8 45%,#6f8f3e 75%,#4e7a2a 100%)"></div></div>
  <div class="abs frame" style="left:469px;top:1175px;width:591px;height:375px"><div role="img" aria-label="Two people carrying a ladder through a garden" style="background:linear-gradient(160deg,#6c8d4b 0%,#3e5f2d 45%,#7f9a6a 70%,#2f4a25 100%)"></div></div>
</section>

<section class="categories">
  <h2 class="abs sec-h serif center" style="top:1632px">Our Categories</h2>
  <p class="abs sec-p center" style="top:1693px">I must explain to you how all this mistaken idea of denouncing pleasure and praising pain was born and I will give you a complete account of the system, and expound the actual teachings of the great explorer of the truth, the master</p>

  <div class="abs cat" style="left:112px;top:1791px">
    <div class="cat-img" role="img" aria-label="Person on a ladder picking fruit" style="background:linear-gradient(160deg,#3d6b2c,#6f9a45 60%,#2c4e22)"></div>
    <div class="cat-icon"><svg width="30" height="34" viewBox="0 0 30 34"><path d="M9 2L4 32M21 2l-5 30M7 10h12M6 18h12M5 26h12" stroke="#333" stroke-width="2" fill="none"/></svg></div>
    <div class="cat-t">Ladder</div>
    <div class="cat-d">I must explain to you how all this mistaken idea of denouncing pleasure and praising</div>
    <div class="cat-l">View Details</div>
  </div>
  <div class="abs cat" style="left:361px;top:1791px">
    <div class="cat-img" role="img" aria-label="Roofer working on a tiled roof" style="background:linear-gradient(160deg,#5a86c0,#b06f4a 55%,#8a4c32)"></div>
    <div class="cat-icon"><svg width="32" height="32" viewBox="0 0 32 32"><path d="M4 28L18 14M14 6l8-2 6 6-2 8-4-4-6 6-4-4 6-6z" stroke="#333" stroke-width="2" fill="none"/></svg></div>
    <div class="cat-t">Hammer</div>
    <div class="cat-d">I must explain to you how all this mistaken idea of denouncing pleasure and praising</div>
    <div class="cat-l">View Details</div>
  </div>
  <div class="abs cat" style="left:610px;top:1791px">
    <div class="cat-img" role="img" aria-label="Family shopping with a trolley" style="background:linear-gradient(160deg,#c9c3b4,#d39a6a 50%,#8e7b6a)"></div>
    <div class="cat-icon"><svg width="32" height="30" viewBox="0 0 32 30"><path d="M2 3h5l4 16h15l3-11H9" stroke="#333" stroke-width="2" fill="none"/><circle cx="13" cy="25" r="2.5" stroke="#333" stroke-width="2" fill="none"/><circle cx="24" cy="25" r="2.5" stroke="#333" stroke-width="2" fill="none"/></svg></div>
    <div class="cat-t">Moving Trolley</div>
    <div class="cat-d">I must explain to you how all this mistaken idea of denouncing pleasure and praising</div>
    <div class="cat-l">View Details</div>
  </div>
  <div class="abs cat" style="left:859px;top:1791px">
    <div class="cat-img" role="img" aria-label="Person resting in a lounge chair" style="background:linear-gradient(160deg,#6a4a36,#b08a6a 55%,#4b3428)"></div>
    <div class="cat-icon"><svg width="28" height="34" viewBox="0 0 28 34"><rect x="6" y="2" width="16" height="14" rx="5" stroke="#333" stroke-width="2" fill="none"/><path d="M3 18h22M14 18v8M6 32l8-6 8 6" stroke="#333" stroke-width="2" fill="none"/></svg></div>
    <div class="cat-t">Chairs</div>
    <div class="cat-d">I must explain to you how all this mistaken idea of denouncing pleasure and praising</div>
    <div class="cat-l">View Details</div>
  </div>
  <div class="abs dot off" style="left:569px;top:2225px"><svg width="8" height="10"><path d="M7 0L1 5l6 5" stroke="#fff" stroke-width="2" fill="none"/></svg></div>
  <div class="abs dot on" style="left:604px;top:2225px"><svg width="8" height="10"><path d="M1 0l6 5-6 5" stroke="#fff" stroke-width="2" fill="none"/></svg></div>
</section>

<section class="why-block">
  <div class="abs why"></div>
  <h2 class="abs sec-h serif center why-h">Why Choose Us</h2>
  <p class="abs sec-p center why-p">I must explain to you how all this mistaken idea of denouncing pleasure and praising pain was born and I will give you a complete account of the system, and expound the actual teachings of the great explorer</p>
  <div class="abs why-ring" style="left:300px;top:2572px"><div><svg width="40" height="30" viewBox="0 0 40 30"><path d="M2 10l8-6 8 4 6-4 14 6M8 12l10 10c2 2 4 0 3-2M14 20l4 4M20 14l8 8" stroke="var(--blue)" stroke-width="2" fill="none"/></svg></div></div>
  <div class="abs why-ring" style="left:549px;top:2572px"><div><svg width="34" height="34" viewBox="0 0 34 34"><circle cx="17" cy="17" r="14" stroke="var(--blue)" stroke-width="2" fill="none"/><path d="M10 22c0-8 6-12 14-12 0 8-4 14-14 12zM10 22l8-6" stroke="var(--blue)" stroke-width="2" fill="none"/></svg></div></div>
  <div class="abs why-ring" style="left:799px;top:2572px"><div><svg width="36" height="32" viewBox="0 0 36 32"><path d="M18 3l7 11M25 14l-6 1M11 14L18 3M4 26l7-12M11 14l2 5M32 26H4M32 26l-7-12M32 26l-3-5" stroke="var(--blue)" stroke-width="2" fill="none"/></svg></div></div>
  <span class="abs why-l" style="left:221px">Locally owned business</span>
  <span class="abs why-l" style="left:470px">Environmentally Friendly</span>
  <span class="abs why-l" style="left:720px">Economically Responsible</span>
</section>

<section class="customers">
  <h2 class="abs sec-h serif center" style="top:2882px">Our Happy Customers</h2>
  <p class="abs sec-p center" style="top:2943px">I must explain to you how all this mistaken idea of denouncing pleasure and praising pain was born and I will give you a complete account of the system, and expound the actual teachings of the great explorer of the truth, the master</p>

  <div class="abs quote" style="left:112px;top:3080px">
    <div class="avatar" role="img" aria-label="Customer portrait" style="background:#c79aa3"></div>
    <div class="q-name serif">Owen Prescott</div>
    <p class="q-text">" I must explain to you how all this mistaken idea of denouncing pleasure and praising pain was born and I will give you a complete account of the system, and expound the actual teachings of the "</p>
    <div class="stars">☆☆☆☆☆</div>
    <div class="q-badge" style="left:212px;background:var(--blue)"></div>
    <div class="q-badge" style="left:246px;background:#3b9a5a"></div>
  </div>
  <div class="abs quote" style="left:445px;top:3051px">
    <div class="avatar" role="img" aria-label="Customer portrait" style="background:#9fb3c9"></div>
    <div class="q-name serif">Lena Morrow</div>
    <p class="q-text">" I must explain to you how all this mistaken idea of denouncing pleasure and praising pain was born and I will give you a complete account of the system, and expound the actual teachings of the "</p>
    <div class="stars">☆☆☆☆☆</div>
    <div class="q-badge" style="left:226px;background:var(--blue)"></div>
    <div class="q-badge" style="left:260px;background:#3b9a5a"></div>
  </div>
  <div class="abs quote" style="left:779px;top:3080px">
    <div class="avatar" role="img" aria-label="Customer portrait" style="background:#b59ac4"></div>
    <div class="q-name serif">Hugh Sanders</div>
    <p class="q-text">" I must explain to you how all this mistaken idea of denouncing pleasure and praising pain was born and I will give you a complete account of the system, and expound the actual teachings of the "</p>
    <div class="stars">☆☆☆☆☆</div>
    <div class="q-badge" style="left:226px;background:var(--blue)"></div>
    <div class="q-badge" style="left:260px;background:#3b9a5a"></div>
  </div>
  <div class="abs dot off" style="left:569px;top:3449px"><svg width="8" height="10"><path d="M7 0L1 5l6 5" stroke="#fff" stroke-width="2" fill="none"/></svg></div>
  <div class="abs dot on" style="left:604px;top:3449px"><svg width="8" height="10"><path d="M1 0l6 5-6 5" stroke="#fff" stroke-width="2" fill="none"/></svg></div>
</section>

<section class="newsletter">
  <div class="abs news"></div>
  <h2 class="abs sec-h serif center news-h">Join To Our Newsletter</h2>
  <p class="abs sec-p center news-p">I must explain to you how all this mistaken idea of denouncing pleasure and praising pain was born and I will give you a complete account of the system, and expound the actual teachings of the great explorer</p>
  <p class="abs news-s center">Best time to get jobs around the house</p>
  <div class="abs news-in">Enter Email Address</div>
  <div class="btn news-btn">Get Discount</div>
</section>

<section class="blogs">
  <h2 class="abs sec-h serif center" style="top:3986px">Latest Blogs</h2>
  <p class="abs sec-p center" style="top:4047px">I must explain to you how all this mistaken idea of denouncing pleasure and praising pain was born and I will give you a complete account of the system, and expound the actual teachings of the great explorer of the truth, the master</p>

  <div class="abs b-img" role="img" aria-label="Hands hammering a nail into wood" style="left:98px;top:4146px;background:linear-gradient(160deg,#d8cfc4,#c28a5a 55%,#9b6a45)"></div>
  <div class="abs b-img" role="img" aria-label="Two people assembling a garden table" style="left:443px;top:4146px;background:linear-gradient(160deg,#8fa37a,#d9dcd6 50%,#6c7f5a)"></div>
  <div class="abs b-img" role="img" aria-label="Sunlit landscaped garden" style="left:787px;top:4146px;background:linear-gradient(160deg,#f2e3b8,#7fa84a 55%,#3f6b28)"></div>

  <article class="abs b-card" style="left:118px;top:4318px">
    <div class="b-date">July 2023</div>
    <div class="b-t">Sed ut perspiciatis unde omnis iste natus error sit voluptatem</div>
    <p class="b-d">Neque porro quisquam est, qui dolorem ipsum quia dolor sit amet, consectetur, adipisci velit, sed quia</p>
    <div class="b-l">Learn More</div>
  </article>
  <article class="abs b-card" style="left:461px;top:4318px;width:280px">
    <div class="b-date">July 2023</div>
    <div class="b-t">Sed ut perspiciatis unde omnis iste natus error sit voluptatem</div>
    <p class="b-d">Neque porro quisquam est, qui dolorem ipsum quia dolor sit amet, consectetur, adipisci velit, sed quia</p>
    <div class="b-l">Learn More</div>
  </article>
  <article class="abs b-card" style="left:806px;top:4318px">
    <div class="b-date">July 2023</div>
    <div class="b-t">Sed ut perspiciatis unde omnis iste natus error sit voluptatem</div>
    <p class="b-d">Neque porro quisquam est, qui dolorem ipsum quia dolor sit amet, consectetur, adipisci velit, sed quia</p>
    <div class="b-l">Learn More</div>
  </article>
</section>

<footer>
  <div class="abs footer"></div>
  <div class="abs f-brand serif">Kerbside Hire</div>
  <div class="abs social" style="left:156px"></div>
  <div class="abs social" style="left:201px"></div>
  <div class="abs social" style="left:248px"></div>
  <div class="abs social" style="left:293px"></div>

  <div class="abs f-h" style="left:492px">Find Us On</div>
  <svg class="abs" style="left:498px;top:4806px" width="11" height="14" viewBox="0 0 12 14"><path d="M6 0C2.7 0 0 2.6 0 5.8 0 10 6 14 6 14s6-4 6-8.2C12 2.6 9.3 0 6 0zm0 8a2.2 2.2 0 110-4.4A2.2 2.2 0 016 8z" fill="var(--blue)"/></svg>
  <p class="abs f-t" style="left:535px;top:4797px">22y, Lorem ipsum is dummy<br>456 987</p>
  <svg class="abs" style="left:496px;top:4891px" width="14" height="12" viewBox="0 0 14 12"><rect width="14" height="12" rx="2" fill="var(--blue)"/><path d="M1 2l6 5 6-5" stroke="#0b0b0b" stroke-width="1.5" fill="none"/></svg>
  <p class="abs f-t" style="left:535px;top:4880px">Monday- Friday: 6:30am – 4:00pm<br>Saturday: 7:30am – 12:00pm<br>Sunday: Closed</p>

  <div class="abs f-h" style="left:887px">Quick Links</div>
  <div class="abs f-link" style="left:887px;top:4811px"><span style="color:var(--blue)">»</span>&nbsp;&nbsp;&nbsp;Payment Terms</div>
  <div class="abs f-link" style="left:887px;top:4838px"><span style="color:var(--blue)">»</span>&nbsp;&nbsp;&nbsp;Hire Aggreement</div>
  <div class="abs f-link" style="left:887px;top:4865px"><span style="color:var(--blue)">»</span>&nbsp;&nbsp;&nbsp;Public Liablity</div>
  <div class="abs f-link" style="left:887px;top:4892px"><span style="color:var(--blue)">»</span>&nbsp;&nbsp;&nbsp;Insurance Coverage</div>

  <p class="abs copy center">© Copyright 2023 | All Rights Reserved.</p>
</footer>

</body>
</html>
```